Tri Fold - Restaurant Brochure & pdf multipage

Develop a product guide specific to "restaurant owners" for our company's restaurant insurance services. It will need to be eye-catching, personal, unique, and industry-specific. Several Insurance flyers from our companies are attached for review. We are happy to provide guidance along the way. Our website is www.kvcoverageteam.example. Please grab logos etc. from there. We can provide other files and more detailed copy.
Updates

Designs look the same

Target Market(s)

Restaurant owners and CFO's

Industry/Entity Type

Insurance Broker

Font styles to use
Other font styles liked:
• match website fonts

Requirements
Must have
• WE WILL PROVIDE DETAILED CONTENT! AT THIS TIME WE ARE LOOKING FOR THE BASIC DESIGN AND LAYOUT.

EYE-CATCHING MODERN DESIGN WITH IMAGES AND BRANDED FEEL. must be print-ready and set up as a PDF to email.

brief description of our agency and its personal boutique feel specializing in the restaurant market. Also, offer a full-service solution to no only manage their business but personal risks too.

Coverages that need to be listed with a brief description: (See attached Flyers)
General Liability
FF&E (Furniture, Fixtures, and Equipment), Property
Workers Compensation
Umbrella
Liquor Liability
Auto
Cyber
Bonds
EPLI

Carrier List:
The Belmoor
Vantry
Oakhollow Shared
Wayfinch
Prairie Motorline
Kelvaro
DRENK
Pellow
CountyMarch
TQV
And many more
Nice to have
• carrier logos if room.
Should not have
• TO BE DETERMINED.

```html
<!DOCTYPE html>
<html lang="en">
<head>
<meta charset="utf-8">
<title>KV Coverage Team – Restaurant Tri-Fold</title>
<link href="https://fonts.googleapis.com/css2?family=Cinzel:wght@500;700&family=Open+Sans:wght@400;600;700&family=Tinos&display=swap" rel="stylesheet">
<style>
:root{
  --red:#e0231f;
  --red-dark:#b3140f;
  --ink:#141414;
  --charcoal:#2a2a2a;
  --paper:#f3f3f3;
  --page-bg:#e4e4e6;
  --white:#ffffff;
  --text-dark:#222;
  --text-light:#e8e8e8;
}
*{margin:0;padding:0;box-sizing:border-box}
html,body{width:874px;height:1200px;overflow:hidden}
body{background:var(--page-bg);font-family:"Open Sans",Arial,sans-serif;color:var(--text-dark);position:relative}
.spread{position:absolute;left:60px;width:672px;height:522px;overflow:hidden;box-shadow:0 10px 12px -6px rgba(0,0,0,.45)}
.spread--outside{top:30px}
.spread--inside{top:612px}
.panel{position:absolute;top:0;height:522px;width:224px;overflow:hidden}
.abs{position:absolute}
.photo{position:absolute}
.serif-head{font-family:"Tinos","Times New Roman",serif;color:var(--red);text-transform:uppercase;letter-spacing:.2px}
.brand{font-family:"Cinzel",Georgia,serif;font-weight:700;letter-spacing:1px;white-space:nowrap}
.small{font-size:5.4px;line-height:1.3}
.sec-title{color:var(--red);font-size:5.6px;font-weight:600;text-transform:uppercase;margin-top:8px}
ul.bullets{list-style:none}
ul.bullets li{padding-left:7px;position:relative}
ul.bullets li::before{content:"";position:absolute;left:1px;top:2.6px;width:2.4px;height:2.4px;background:var(--red)}
p.just{text-align:justify}

/* outside spread */
.panel--markets{left:0;background:linear-gradient(180deg,#fff 30%,#e9e9e9)}
.panel--bop{left:224px;background:linear-gradient(180deg,#1c1c1c,#2e2e2e 60%,#1a1a1a);color:var(--text-light)}
.panel--cover{left:448px;background:var(--paper)}
.markets-body{position:absolute;left:14px;top:178px;width:198px}
.markets-body h2{font-size:11px;font-weight:400}
.rule{width:26px;height:1.5px;background:var(--red);margin:8px 0 6px}
.bop-logo{position:absolute;left:0;width:224px;top:150px;text-align:center;color:var(--white);font-size:15px}
.bop-title{position:absolute;top:190px;left:0;width:224px;text-align:center;font-size:9.5px;font-weight:400}
.bop-copy{position:absolute;left:16px;top:212px;width:194px}
.bop-copy p{margin-bottom:9px}
.hl{color:var(--red)}
.contact-title{position:absolute;top:385px;width:224px;text-align:center;font-size:8px;font-family:"Tinos",serif;color:var(--red)}
.contact-web{position:absolute;top:396px;width:224px;text-align:center}
.office{position:absolute;top:424px;width:90px}
.office b{color:var(--red);font-weight:700}
.office--a{left:40px}
.office--b{left:122px}
.agent{position:absolute;top:478px;width:224px;text-align:center}
.cover-logo{position:absolute;top:36px;left:0;width:224px;text-align:center;color:var(--white);font-size:17px}
.cover-logo small{display:block;font-size:6px;letter-spacing:2px;color:var(--red);margin-top:3px;font-weight:500}
.cover-band{position:absolute;left:0;width:224px;text-align:center;color:var(--white)}
.cover-band.kicker{top:432px;font-weight:700;font-size:7.4px;line-height:1.45}
.cover-band.slogan{top:458px;font-family:"Cinzel",serif;font-weight:700;font-size:8.6px;line-height:1.35}
.url-bar{position:absolute;left:28px;top:493px;width:186px;height:15px;background:var(--ink);color:var(--white);font-size:7.4px;font-weight:600;letter-spacing:.8px;text-align:center;line-height:15px}

/* inside spread */
.panel--story{left:0;background:linear-gradient(180deg,#0f0f0f,#2b2b2b 55%,#1e1e1e);color:var(--text-light)}
.story-head{position:absolute;left:14px;top:16px;width:200px}
.story-head h2{font-size:8.6px;font-family:"Tinos",serif;color:var(--red);font-weight:400}
.story-head p{font-size:6px;font-family:"Tinos",serif;color:var(--red)}
.story-copy{position:absolute;left:14px;top:50px;width:198px}
.story-copy p{margin-bottom:7px}
.lists{position:absolute;top:268px;left:14px;width:200px}
.lists h3{font-family:"Tinos",serif;font-weight:400;color:var(--red);font-size:9px;position:absolute;top:0}
.lists ul{position:absolute;top:13px}
.col-carriers{left:0}
.col-cover{left:80px}
.panel--alacarte{left:224px;width:448px;background:var(--paper)}
.alc-head{position:absolute;left:12px;top:222px;font-size:9.6px;line-height:1.3;font-weight:400}
.alc-logo{position:absolute;right:14px;top:224px;font-size:15px;color:#3a3a3a}
.alc-intro{position:absolute;left:12px;top:262px;width:420px;font-size:6.4px;line-height:1.3}
.item{position:absolute;width:196px;display:flex;gap:6px}
.icon{flex:0 0 24px;height:24px;border:1px solid #999;background:#fff;display:flex;align-items:center;justify-content:center}
.item b{color:var(--red);font-weight:700}
.item p{font-size:5.4px;line-height:1.25}
.alc-band{position:absolute;right:22px;color:var(--white);font-weight:700;font-size:7px;text-align:right;white-space:nowrap}
</style>
</head>
<body>

<section class="spread spread--outside" aria-label="Brochure outside spread">

  <div class="panel panel--markets">
    <div class="photo" role="img" aria-label="Photo of a smiling server holding a glass cloche over a pastry counter" style="left:0;top:0;width:224px;height:172px;background:linear-gradient(135deg,#6f5a48,#c4a789 55%,#8a7462);clip-path:polygon(0 0,100% 0,100% 82%,0 100%)"></div>
    <svg class="abs" style="left:0;top:130px" width="224" height="50" viewBox="0 0 224 50">
      <path d="M0 42 Q110 34 224 8 L224 13 Q110 40 0 47Z" fill="var(--red)"/>
      <path d="M0 47 Q110 40 224 13 L224 20 Q110 46 0 50Z" fill="#cfcfcf"/>
    </svg>
    <div class="markets-body small">
      <h2 class="serif-head">Many markets offer:</h2>
      <div class="rule"></div>
      <div class="sec-title" style="margin-top:0">Workers' Compensation Compensation</div>
      <p class="just">Your employees are important to the success of your restaurant. If an employee gets injured on the job, you can count on help return that worker to health and productivity quickly. Our approach to managing claims promotes better outcomes and helps keep medical costs low, which could have a positive impact on your future premiums.</p>
      <div class="sec-title" style="margin-top:14px">Payroll Billing</div>
      <p>Help improve the cash flow of your business.</p>
      <ul class="bullets">
        <li>ZERO down payment</li>
        <li>NO monthly billing or finance fees</li>
        <li>NO service charges</li>
        <li>NO more late payments</li>
        <li>MINIMAL audit adjustments</li>
      </ul>
      <div class="sec-title">24/7 My Account Access</div>
      <p>My Account offers 24/7 policy access to a number of simple services anytime, and anywhere it's convenient.</p>
      <ul class="bullets">
        <li>Pay online, there's even AutoPay so you'll never miss a payment</li>
        <li>Go paperless to receive documents and state ments via email</li>
        <li>Send us documents electronically with our easy upload feature</li>
        <li>Get most Certificates of Insurance instantly</li>
        <li>File a claim at your convenience</li>
        <li>Track status and payments with realtime updates</li>
      </ul>
      <div class="sec-title">Business Auto</div>
      <p class="just">The Business Auto policy combines innovative product features, safe choice discounts and exceptional claim service. Our Accident Forgiveness Program recognizes that "bad things happen to good people." So customers with safe driving records aren't penalized for "nuisance" claims or charged for an accident if they've been claim free.</p>
    </div>
  </div>

  <div class="panel panel--bop">
    <svg class="abs" style="left:0;top:0" width="224" height="522" viewBox="0 0 224 522">
      <circle cx="106" cy="70" r="57" fill="none" stroke="var(--red)" stroke-width="2.5"/>
      <path d="M150 522 L224 470 L224 522Z" fill="var(--red)"/>
      <path d="M120 522 Q190 500 224 455 L224 462 Q192 505 132 522Z" fill="#cfcfcf"/>
    </svg>
    <div class="photo" role="img" aria-label="Circular photo of a chef drizzling sauce over a plated dish" style="left:52px;top:16px;width:108px;height:108px;border-radius:50%;background:radial-gradient(circle at 50% 60%,#8a5a3a,#2a1c14 70%)"></div>
    <div class="bop-logo brand">KV COVERAGE TEAM</div>
    <div class="bop-title serif-head">Business Owner's Policy (BOP)</div>
    <div class="bop-copy small">
      <p class="just">A BOP can help protect your business in much the same way that a homeowners policy protects your home and personal possessions. The BOP combines these essential coverages to provide a cost-effective solution to help safeguard your restaurant:</p>
      <p><span class="hl">Business Property insurance</span> to help protect the property you own, lease or rent</p>
      <p><span class="hl">Business Liability coverage</span> to help protect your business in the event it is responsible for causing harm to a person and/or damage to property</p>
      <p><span class="hl">Business Income coverage</span> to help protect lost income if your business is forced to close due to direct physical loss or damage to its premises resulting from a covered cause of loss</p>
    </div>
    <div class="contact-title">CONTACT INFO</div>
    <div class="contact-web small">www.servesafecover.example - owned by KV Coverage Team LLC<br>www.kvcoverageteam.example</div>
    <div class="office office--a small"><b>NORTHBROOK RIDGE</b><br>18 Larkspur Ave<br>Northbrook Ridge, ST 10421<br>555-014-2280</div>
    <div class="office office--b small"><b>HALDEN - LAKE MARROW</b><br>702 Orchard Loop Suite 4<br>Halden, ST 10488<br>555-019-6410</div>
    <div class="agent small">Marlow T. Keene, CLCS, SBCS - President<br>marlow@kvcoverageteam.example | Direct: 555-017-3392</div>
  </div>

  <div class="panel panel--cover">
    <div class="abs" style="left:0;top:0;width:224px;height:140px;background:linear-gradient(180deg,#0d0d0d,#2a2a2a)"></div>
    <div class="cover-logo brand">KV COVERAGE TEAM<small>INSURANCE · RISK MANAGEMENT</small></div>
    <div class="photo" role="img" aria-label="Photo of a smiling chef in white jacket and toque, arms crossed, in a restaurant kitchen" style="left:0;top:100px;width:224px;height:350px;background:linear-gradient(160deg,#9a8f86,#d6d2cc 40%,#6a5c52 75%,#3a302a);clip-path:polygon(0 8%,100% 0,100% 92%,0 100%)"></div>
    <svg class="abs" style="left:0;top:400px" width="224" height="122" viewBox="0 0 224 122">
      <path d="M0 30 Q120 22 224 0 L224 122 L0 122Z" fill="var(--red)"/>
    </svg>
    <div class="cover-band kicker">SMALL COMMERCIAL<br>SMALL BUSINESS OWNERS | RESTAURANTS</div>
    <div class="cover-band slogan">YOU WORK HARD SERVING OTHERS,<br>HERE'S HOW WE CAN SERVE YOU.</div>
    <div class="url-bar">www.kvcoverageteam.example</div>
  </div>
</section>

<section class="spread spread--inside" aria-label="Brochure inside spread">

  <div class="panel panel--story">
    <div class="story-head">
      <h2>KV Coverage Team Knows Restaurants!</h2>
      <p>You work hard serving others here's how we can serve you.</p>
    </div>
    <div class="story-copy small">
      <p class="just">Starting in the restaurant business is daunting. Running the restaurant is demanding. Growing a business is difficult. Add unpredictable circumstances that may ruin the balance you have established and you end up with a company incapable of taking a hit, and an owner perpetually worried about it actually happening.</p>
      <p class="just">This applies not only to businesses but to one's personal property as well. The common solution, of course, is insurance, something that is tricky to furnish in itself. Not knowing what to search for in the first place makes shopping for a risk management plan a tricky, yet necessary, decision to make. With KV Coverage Team, you will know the policies you are supposed to have, why you are supposed to have them, and how much they are supposed to cost. After all, the best business owners only rest easy once they have inspected and ironed out every single detail.</p>
      <p class="just">Different problems necessitate different plans, which is why risk management for your restaurant should never be a one-size-fits-all deal. When it comes to restaurant insurance our company stands out as the top provider of personalized plans that work according to how you restaurant business operates, not by what passes as sufficient coverage on paper.</p>
      <p class="just">Your organization can depend on the vast number of carriers we work with—all A-rated or better. Our team can lend you the skills and experience necessary to design an insurance plan that suits the specific needs of your restaurant business. Trust us to deliver risk management strategies that are as unique as your business and as effective as you want them to be.</p>
    </div>
    <div class="lists small">
      <h3 class="col-carriers">CARRIERS:</h3>
      <ul class="bullets col-carriers">
        <li>The Belmoor</li><li>Vantry</li><li>Oakhollow Shared</li><li>Wayfinch</li><li>Prairie Motorline</li><li>Kelvaro</li><li>DRENK</li><li>Pellow</li><li>CountyMarch</li><li>TQV</li>
      </ul>
      <h3 class="col-cover">COMMON COVERAGES</h3>
      <ul class="bullets col-cover">
        <li>General Liability</li><li>FF&amp;E (Furniture, Fixtures,<br>&amp; Equipment), Property</li><li>Workers Compensation</li><li>Umbrella</li><li>Liquor Liability</li><li>Auto</li><li>Cyber</li><li>Bonds</li><li>EPLI</li>
      </ul>
    </div>
    <svg class="abs" style="left:0;top:400px" width="224" height="122" viewBox="0 0 224 122">
      <path d="M0 40 L224 4 L224 12 L0 48Z" fill="var(--red)"/>
    </svg>
    <div class="photo" role="img" aria-label="Photo of a chef plating food in a restaurant kitchen" style="left:0;top:412px;width:224px;height:110px;background:linear-gradient(150deg,#d8d4cf,#8f8378 50%,#3b332d);clip-path:polygon(0 33%,100% 0,100% 100%,0 100%)"></div>
  </div>

  <div class="panel panel--alacarte">
    <div class="photo" role="img" aria-label="Photo of a server taking orders from smiling diners at a restaurant table" style="left:0;top:0;width:448px;height:214px;background:linear-gradient(100deg,#4a3a30,#9c7f66 35%,#c7b39d 55%,#6e5848 80%,#3a2e26)"></div>
    <svg class="abs" style="left:0;top:180px" width="448" height="50" viewBox="0 0 448 50">
      <path d="M0 32 Q120 20 220 34 Q330 50 448 22 L448 50 L0 50Z" fill="var(--paper)"/>
    </svg>
    <h2 class="alc-head serif-head">Examples of À la carte coverages<br>restaurants like yours select</h2>
    <div class="alc-logo brand">KV COVERAGE TEAM</div>
    <p class="alc-intro">A wide range of optional coverages offer additional protection for risks that are unique to restaurants. Many are available separately or in cost-effective packages, giving you the flexibility to design a program that's important to your business.</p>

    <div class="item" style="left:12px;top:300px">
      <div class="icon"><svg width="14" height="14" viewBox="0 0 14 14"><path d="M7 1 L12 3 V7 Q12 11 7 13 Q2 11 2 7 V3Z" fill="none" stroke="#444"/></svg></div>
      <p><b>DATA BREACH</b> helps you pay for response expenses, legal costs and income protection if the sensitive personal information you collect or store is lost or stolen.</p>
    </div>
    <div class="item" style="left:12px;top:345px">
      <div class="icon"><svg width="14" height="14" viewBox="0 0 14 14"><path d="M1 5 L7 1 L13 5 M2 6 V12 M5 6 V12 M9 6 V12 M12 6 V12 M1 13 H13" fill="none" stroke="#444"/></svg></div>
      <p><b>EMPLOYMENT PRACTICES LIABILITY (EPL)</b> provides coverage if you're sued by an employee, patron or vendor alleging discrimination, sexual harassment, wrongful termination or other types of claims relating to your employment practices.</p>
    </div>
    <div class="item" style="left:12px;top:398px">
      <div class="icon"><svg width="14" height="14" viewBox="0 0 14 14"><path d="M4 2 H10 L9 7 H5Z M7 7 V12 M4 12 H10" fill="none" stroke="#444"/></svg></div>
      <p><b>LIQUOR LIABILITY</b> helps cover your legal costs, court fees and any civil or criminal damages resulting from the sale of liquor at your restaurant.</p>
    </div>
    <div class="item" style="left:12px;top:440px">
      <div class="icon"><svg width="14" height="14" viewBox="0 0 14 14"><path d="M3 1 H9 L11 3 V13 H3Z M5 6 H9 M5 8 H9 M5 10 H8" fill="none" stroke="#444"/></svg></div>
      <p><b>FRANCHISE UPGRADE</b> helps pay additional costs a franchisee may incur to upgrade damaged property to franchise standards following a covered loss.</p>
    </div>
    <div class="item" style="left:12px;top:478px">
      <div class="icon"><svg width="14" height="14" viewBox="0 0 14 14"><path d="M1 7 L7 2 L13 7 M3 6 V12 H11 V6" fill="none" stroke="#444"/></svg></div>
      <p><b>BUSINESS INCOME FOR FOOD CONTAMINATION</b> provides coverage for lost income if your operations are suspended by a public health authority due to the discovery of food contamination.</p>
    </div>

    <div class="item" style="left:240px;top:300px">
      <div class="icon"><svg width="14" height="14" viewBox="0 0 14 14"><path d="M3 10 Q1 10 1 8 Q1 6 3 6 Q4 3 7 3 Q10 3 11 6 Q13 6 13 8 Q13 10 11 10Z" fill="none" stroke="#444"/></svg></div>
      <p><b>BUSINESS INCOME FOR CLOUD SERVICE INTERRUPTION</b> helps pay for lost income if your provider suspends or slows business operations because of an unplanned and unannounced interruption in your cloud service.</p>
    </div>
    <div class="item" style="left:240px;top:353px">
      <div class="icon"><svg width="14" height="14" viewBox="0 0 14 14"><circle cx="4" cy="5" r="2" fill="none" stroke="#444"/><circle cx="10" cy="5" r="2" fill="none" stroke="#444"/><path d="M1 12 Q4 8 7 12 Q10 8 13 12" fill="none" stroke="#444"/></svg></div>
      <p><b>EMPLOYEE DISHONESTY</b> provides coverage if an employee steals money, securities or other property owned by your business.</p>
    </div>
    <div class="item" style="left:240px;top:392px">
      <div class="icon"><svg width="14" height="14" viewBox="0 0 14 14"><path d="M2 10 Q2 4 7 4 Q12 4 12 10Z M1 11 H13 M7 2 V4" fill="none" stroke="#444"/></svg></div>
      <p><b>SPOILAGE</b> provides coverage for the cost of food or income that's lost due to a breakdown or failure of heating or cooling equipment, power failure or contamination by a refrigerant.</p>
    </div>
    <div class="item" style="left:240px;top:432px">
      <div class="icon"><svg width="14" height="14" viewBox="0 0 14 14"><rect x="2" y="2" width="10" height="7" fill="none" stroke="#444"/><path d="M5 12 H9 M7 9 V12" stroke="#444"/></svg></div>
      <p><b>ELECTRONIC DATA AND INTERRUPTION OF COMPUTER OPERATIONS</b> pays to replace or restore electronic data that has been destroyed, corrupted, or made inaccessible by a computer virus or covered loss, and any loss of business income.</p>
    </div>

    <svg class="abs" style="left:0;top:470px" width="448" height="52" viewBox="0 0 448 52">
      <path d="M90 52 C200 20 300 5 448 0 L448 52Z" fill="var(--red)"/>
    </svg>
    <div class="alc-band" style="top:490px">OUR OPTIONAL COVERAGES DON'T STOP HERE</div>
    <div class="alc-band" style="top:504px;font-size:7.6px">Call us today
      <svg width="8" height="8" viewBox="0 0 10 10" style="vertical-align:-1px;margin:0 3px"><circle cx="5" cy="5" r="4.4" fill="none" stroke="#fff"/><path d="M3.3 2.6 L4.3 3.9 L3.8 4.5 Q4.6 5.8 5.6 6.2 L6.1 5.7 L7.4 6.7 L6.8 7.4 Q4.7 7.3 2.6 3.2Z" fill="#fff"/></svg>
      555-019-6410</div>
  </div>
</section>

</body>
</html>
```